Website for Cedar Brook Fellowship Church

Wordpress website design required for Cedar Brook Fellowship Church. We are a family oriented church catering for age groups from school age to elderly people. The church has a wide variety of activities which it coordinates. The idea is to describe the activities on the activities page, but cross-link them to show which would be applicable to the different age groups.

We would like an inviting website which is easy to read and navigate.

Target Market(s)

Very wide audience - from school age youth to elderly people, so design and style should cater for both audiences.

Industry/Entity Type

Church

Coding

Coded - Design and coding required

Number of Pages Required

5+ page

Font styles to use
Sans Serif

Colors
0255a3
ffffff
0792cd
f78f20

Requirements
Must have
• Inviting website.
• Clear readable font.
• Space to import photos to balance text on each page.
• Need to project a dynamic and progressive feel for the church.
• Easy to navigate.
Nice to have
• Scrolling photos on pages. Ability to enter questions/ comments/prayer requests on Home page.
Should not have
• Conservative audience, so should not be too bold.

```html
<!DOCTYPE html>
<html lang="en">
<head>
<meta charset="utf-8">
<title>Cedar Brook Fellowship Church</title>
<link rel="stylesheet" href="https://fonts.googleapis.com/css2?family=Arimo:wght@400;700&family=Noto+Serif:wght@400&family=Yesteryear&family=Satisfy&display=swap">
<style>
  :root {
    --brand-blue: #0255a3;
    --sky-blue: #0792cd;
    --accent-orange: #f78f20;
    --white: #ffffff;
    --ink: #111111;
    --photo-warm: #c79a7c;
    --photo-dark: #3b3f48;
  }
  * { margin: 0; padding: 0; box-sizing: border-box; }
  html, body { width: 958px; height: 1200px; overflow: hidden; background: var(--white); }
  body { position: relative; font-family: "Arimo", Arial, sans-serif; color: var(--ink); }

  .site-header { position: absolute; top: 0; left: 0; width: 958px; height: 149px; }
  .brand { position: absolute; top: 68px; left: 0; width: 958px; display: flex; justify-content: center; align-items: center; gap: 8px; }
  .brand-dot { width: 11px; height: 11px; border-radius: 50%; background: var(--brand-blue); }
  .brand-name { font-family: "Arimo", Arial, sans-serif; font-size: 17px; color: var(--brand-blue); }

  .main-nav { position: absolute; top: 130px; left: 55px; width: 843px; height: 36px; background: var(--brand-blue); border: 1px solid #3a6fa8; z-index: 2; display: flex; justify-content: center; align-items: center; gap: 30px; }
  .main-nav a { color: var(--white); text-decoration: none; font-size: 14px; letter-spacing: 0.2px; }

  .hero-photo { position: absolute; top: 149px; left: 0; width: 958px; height: 268px; background: linear-gradient(180deg, var(--photo-dark) 0%, var(--photo-warm) 35%, #d8ad8f 65%, #7c6a5e 100%); }

  .welcome-band { position: absolute; top: 421px; left: 0; width: 958px; height: 165px; background: var(--sky-blue); text-align: center; }
  .welcome-title { margin-top: 46px; font-size: 30px; font-weight: 700; color: var(--brand-blue); }
  .welcome-title small { font-size: 24px; font-weight: 400; }
  .welcome-name { font-family: "Yesteryear", cursive; font-size: 31px; color: var(--white); margin-top: 2px; }
  .band-notch { position: absolute; top: 555px; left: 446px; width: 62px; height: 62px; border-radius: 50%; background: var(--sky-blue); z-index: -1; }

  .mission { position: absolute; top: 659px; left: 130px; width: 698px; text-align: center; }
  .mission h2 { font-size: 16px; font-weight: 700; }
  .mission p { font-family: "Satisfy", cursive; font-size: 17px; line-height: 25px; margin-top: 17px; }

  .feature-card { position: absolute; top: 823px; left: 55px; width: 843px; height: 223px; background: var(--white); box-shadow: 0 2px 5px rgba(0,0,0,0.45); border: 1px solid #ddd; }
  .feature { position: absolute; top: 0; width: 260px; }
  .feature h3 { position: absolute; top: 28px; left: 0; font-family: "Noto Serif", Georgia, serif; font-weight: 400; font-size: 14px; letter-spacing: 0.6px; color: var(--brand-blue); white-space: nowrap; }
  .feature-photo { position: absolute; top: 68px; left: 1px; width: 88px; height: 55px; }
  .feature p { position: absolute; top: 69px; left: 99px; width: 160px; font-size: 12.3px; line-height: 15px; }
  .read-more { position: absolute; top: 146px; left: 99px; font-size: 12.5px; font-weight: 700; color: var(--accent-orange); text-decoration: none; }
  .read-more-arrow { position: absolute; top: 148px; left: 222px; }
  .photo-study { background: linear-gradient(135deg, #1d1a18, #6b4b30 55%, #d9d3cc); }
  .photo-group { background: linear-gradient(180deg, #6fb3e4, #c99b80 55%, #f2f2f2); }
  .photo-prayer { background: linear-gradient(90deg, #141010, #a8745a 55%, #2a1a14); }

  .site-footer { position: absolute; top: 1081px; left: 0; width: 958px; height: 119px; background: var(--brand-blue); color: var(--white); }
  .footer-mark { position: absolute; top: 32px; left: 57px; width: 34px; height: 34px; border-radius: 50%; background: var(--white); }
  .footer-copy { position: absolute; top: 34px; left: 100px; font-size: 10.5px; line-height: 13px; }
  .footer-block { position: absolute; top: 38px; font-size: 10.5px; line-height: 13px; }
  .footer-block h4 { font-size: 14px; font-weight: 400; letter-spacing: 0.3px; margin-bottom: 1px; }
  .footer-follow { position: absolute; top: 40px; left: 688px; font-size: 10px; display: flex; align-items: center; gap: 6px; }
  .follow-dot { width: 8px; height: 8px; border-radius: 50%; background: var(--white); }
</style>
</head>
<body>
  <header class="site-header">
    <div class="brand"><span class="brand-dot"></span><span class="brand-name">Cedar Brook Fellowship Church</span></div>
    <nav class="main-nav">
      <a href="#">HOME</a><a href="#">ABOUT US</a><a href="#">AGE GROUP</a><a href="#">ACTIVITIES</a><a href="#">EVENTS</a><a href="#">CONTACT</a>
    </nav>
  </header>

  <div class="hero-photo" role="img" aria-label="Photo of many hands stacked together in unity"></div>

  <div class="band-notch"></div>
  <section class="welcome-band">
    <h1 class="welcome-title">Welcome <small>to</small></h1>
    <p class="welcome-name">Cedar Brook Fellowship Church</p>
  </section>

  <section class="mission">
    <h2>OUR MISSION</h2>
    <p>Ut enim ad minima veniam, quis nostrum exercitationem ullam corporis suscipit laboriosam, nisi ut aliquid ex ea commodi consequatur? Quis autem vel eum iure reprehenderit qui in ea voluptate velit esse quam nihil molestiae consequatur, vel illum qui dolorem eum fugiat quo voluptas nulla pariatur?</p>
  </section>

  <section class="feature-card">
    <article class="feature" style="left:20px">
      <h3>MESSAGES</h3>
      <div class="feature-photo photo-study" role="img" aria-label="Photo of hands holding an open Bible"></div>
      <p>Sed ut perspiciatis unde omnis iste natus error sit voluptatem accusantium doloremque.</p>
      <a class="read-more" href="#">Read more</a>
      <svg class="read-more-arrow" width="14" height="10" viewBox="0 0 14 10"><path d="M0 0 L14 5 L0 10 L4 5 Z" fill="var(--brand-blue)"/></svg>
    </article>
    <article class="feature" style="left:300px">
      <h3>NEWS</h3>
      <div class="feature-photo photo-group" role="img" aria-label="Photo of a cheerful group of young people"></div>
      <p>Nemo enim ipsam voluptatem quia voluptas sit aspernatur aut odit aut fugit, sed quia.</p>
      <a class="read-more" href="#">Read more</a>
      <svg class="read-more-arrow" width="14" height="10" viewBox="0 0 14 10"><path d="M0 0 L14 5 L0 10 L4 5 Z" fill="var(--brand-blue)"/></svg>
    </article>
    <article class="feature" style="left:581px">
      <h3>PRAYER REQUESTS</h3>
      <div class="feature-photo photo-prayer" role="img" aria-label="Photo of a person praying with folded hands"></div>
      <p>Neque porro quisquam est, qui dolorem ipsum quia dolor sit amet, consectetur, adipisci veli,</p>
      <a class="read-more" href="#">Read more</a>
      <svg class="read-more-arrow" width="14" height="10" viewBox="0 0 14 10"><path d="M0 0 L14 5 L0 10 L4 5 Z" fill="var(--brand-blue)"/></svg>
    </article>
  </section>

  <footer class="site-footer">
    <div class="footer-mark"></div>
    <p class="footer-copy">Copyright © 2016.<br>Cedar Brook Fellowship Church<br>All Rights Reserved</p>
    <div class="footer-block" style="left:267px">
      <h4>SERVICE TIMES:</h4>
      <p>xx:xxam - xx:xxam<br>xx:xxpm- xx:xxpm</p>
    </div>
    <div class="footer-block" style="left:477px">
      <h4>CONTACT INFORMATION:</h4>
      <p>Address<br>Phone Numbers</p>
    </div>
    <div class="footer-follow"><span>FOLLOW US</span><span class="follow-dot"></span></div>
  </footer>
</body>
</html>
```